Attract renters to our neighborhoods - inform renters who we are

Apartments in several neighborhoods. We want to attract renters who want to live along the lake or other near by neighborhoods. We want them to know that we have an apartment for them in their location.
The perfect location to spend your time.
When minutes matter LIVE where you work and play! (love this tag line)
Updates

www.kvtresidences.example Choose from over 3,700 apartments in Chicago’s most celebrated neighborhoods. 773-582-6041 Chicago’s most celebrated neighborhoods. 31 PROPERTIES

Target Market(s)

Sophisticated apartment renter who wants location, space, amenities

Industry/Entity Type

Apartment Rentals

Requirements
Must have
• Feel like I want to live there, or the ad is calling me
Nice to have
• Appeal to a sophisticated apartment renter. We have what you want, where you want to be.
Should not have
• Logo colors are black and red/burnt orange see attached logo

```html
<!DOCTYPE html>
<html lang="en">
<head>
<meta charset="utf-8">
<title>KVT Residences – When Minutes Matter</title>
<link rel="stylesheet" href="https://fonts.googleapis.com/css2?family=Josefin+Sans:wght@400;600;700&family=Great+Vibes&family=Sacramento&family=Montserrat:wght@600;700&display=swap">
<style>
  :root{
    --red:#c4121a;
    --deep-red:#a8141b;
    --ink:#1d1d1f;
    --white:#ffffff;
    --paper:#f6f6f6;
  }
  *{margin:0;padding:0;box-sizing:border-box}
  html,body{width:902px;height:1200px;overflow:hidden;background:var(--paper)}
  .flyer{position:relative;width:902px;height:1200px;overflow:hidden;background:var(--white);font-family:'Josefin Sans',sans-serif}
  .hero-photo{position:absolute;left:0;top:0;width:902px;height:620px;
    background:linear-gradient(180deg,#3a4048 0%,#2c3540 35%,#343a42 70%,#4a4a4c 100%)}
  .shapes{position:absolute;left:0;top:0}
  .headline{position:absolute;left:68px;top:0;width:530px;height:500px;color:var(--white)}
  .when{position:absolute;top:52px;left:0;font-family:'Great Vibes',cursive;font-size:92px;line-height:1}
  .minutes{position:absolute;top:172px;left:6px;font-size:52px;font-weight:400;letter-spacing:1px;white-space:nowrap}
  .live{position:absolute;top:258px;left:-14px;font-size:230px;font-weight:400;color:var(--red);line-height:.8;letter-spacing:-6px;transform:scaleY(1.12);transform-origin:left top;white-space:nowrap}
  .work-play{position:absolute;top:463px;left:6px;font-size:29px;font-weight:600;white-space:nowrap;letter-spacing:.5px}
  .tagline{position:absolute;left:62px;top:622px;font-family:'Sacramento',cursive;font-size:84px;color:var(--deep-red);line-height:.87;font-weight:400;white-space:nowrap}
  .tagline span{display:block}
  .tagline span+span{margin-left:-12px}
  .offer{position:absolute;left:52px;top:806px;white-space:nowrap}
  .offer .count{color:var(--ink);font-size:38px;line-height:46px;display:block}
  .offer .detail{color:var(--deep-red);display:block;font-size:31.5px;line-height:43px;margin-top:11px}
  .brand{position:absolute;left:40px;top:1034px;font-size:80px;font-weight:700;color:var(--ink);letter-spacing:-1px;line-height:1}
  .brand-rule{position:absolute;left:0;top:1150px;width:240px;height:3px;background:var(--red)}
  .call-box{position:absolute;left:245px;top:1006px;width:358px;height:114px;background:var(--ink);padding:14px 14px 0 16px}
  .call-box .cta{color:var(--red);font-size:29px;letter-spacing:1px;display:block}
  .call-box .phone{display:flex;align-items:center;gap:16px;margin-top:10px;color:var(--white);font-family:'Montserrat',sans-serif;font-weight:600;font-size:41px;white-space:nowrap}
  .web{position:absolute;left:257px;top:1136px;display:flex;align-items:center;gap:12px;color:var(--red);font-size:25px;white-space:nowrap}
  .column{position:absolute;left:603px;top:0;width:299px;height:1200px}
  .tile{position:absolute;left:25px;width:216px;border:2px solid var(--white)}
  .tile-label{position:absolute;left:0;width:266px;text-align:center;color:var(--white);font-weight:600;font-size:16px;line-height:1.25;letter-spacing:.5px}
  .sky-city{background:linear-gradient(180deg,#3d8fd8 0%,#8bb6d9 25%,#7d8a95 55%,#5c6c76 80%,#3fa7b3 100%)}
  .lake-city{background:linear-gradient(180deg,#7fb1e0 0%,#c9d8e4 25%,#8b9098 55%,#6f7a80 85%,#4c8aa0 100%)}
  .beach{background:linear-gradient(180deg,#9fc4e5 0%,#c7d5d8 22%,#4c6f4f 45%,#2ba4a8 70%,#d8c7a5 85%,#1b9eb0 100%)}
</style>
</head>
<body>
<main class="flyer">
  <div class="hero-photo" role="img" aria-label="Aerial view of Chicago skyline at dusk with the lakefront"></div>

  <svg class="shapes" width="902" height="1200" viewBox="0 0 902 1200" aria-hidden="true">
    <polygon points="0,500 318,604 603,555 603,1200 0,1200" fill="#ffffff"/>
    <polygon points="0,478 318,582 603,534 603,548 318,604 0,500" fill="#c4121a"/>
    <polygon points="0,478 0,492 318,596 318,582" fill="#ffffff"/>
    <polygon points="603,92 885,20 902,20 902,1200 603,1200" fill="#b3151b"/>
    <rect x="885" y="20" width="17" height="1180" fill="#8f1016"/>
  </svg>

  <section class="headline">
    <div class="when">When</div>
    <div class="minutes">MINUTES MATTER</div>
    <div class="live">LIVE</div>
    <div class="work-play">WHERE YOU WORK AND PLAY!</div>
  </section>

  <p class="tagline"><span>The perfect location</span><span>to spend your time.</span></p>

  <p class="offer">
    <span class="count">CHOOSE FROM OVER 3,700</span>
    <span class="detail">APARTMENTS IN CHICAGO’S MOST<br>CELEBRATED NEIGHBORHOODS.</span>
  </p>

  <div class="brand">KVT</div>
  <div class="brand-rule"></div>

  <div class="call-box">
    <span class="cta">CALL US TODAY!</span>
    <span class="phone">
      <svg width="30" height="30" viewBox="0 0 30 30" aria-hidden="true">
        <circle cx="15" cy="15" r="13" fill="none" stroke="#c4121a" stroke-width="2"/>
        <path d="M10 8.5c1-.8 2-.6 2.5.3l1.2 2.3c.4.8.1 1.5-.6 2l-.8.6c.8 1.7 2 2.9 3.7 3.7l.6-.8c.5-.7 1.2-1 2-.6l2.3 1.2c.9.5 1.1 1.5.3 2.5-1.2 1.5-3 1.8-5.2.6-2.6-1.4-4.6-3.4-6-6-1.2-2.2-.9-4 .6-5.2z" fill="#c4121a"/>
      </svg>
      773-582-6041
    </span>
  </div>

  <div class="web">
    <svg width="16" height="16" viewBox="0 0 16 16" aria-hidden="true">
      <circle cx="8" cy="8" r="7" fill="none" stroke="#1d1d1f" stroke-width="1.4"/>
      <ellipse cx="8" cy="8" rx="3" ry="7" fill="none" stroke="#1d1d1f" stroke-width="1.2"/>
      <line x1="1" y1="8" x2="15" y2="8" stroke="#1d1d1f" stroke-width="1.2"/>
    </svg>
    www.kvtresidences.example
  </div>

  <aside class="column">
    <div class="tile sky-city" style="top:64px;height:240px" role="img" aria-label="Aerial photo of Gold Coast and Old Town along the lakefront"></div>
    <div class="tile-label" style="top:323px">GOLD COAST &amp;<br>OLD TOWN</div>

    <div class="tile lake-city" style="top:381px;height:210px" role="img" aria-label="Aerial photo of River North high-rises"></div>
    <div class="tile-label" style="top:612px">RIVER NORTH</div>

    <div class="tile beach" style="top:639px;height:210px" role="img" aria-label="Aerial photo of Lincoln Park beach and lake"></div>
    <div class="tile-label" style="top:870px">LINCOLN PARK</div>

    <div class="tile lake-city" style="top:901px;height:208px" role="img" aria-label="Aerial photo of Lakeview skyline by the lake"></div>
    <div class="tile-label" style="top:1130px">LAKEVIEW</div>
  </aside>
</main>
</body>
</html>
```